Budget planning & tracking app

I want to make personal budget planning and tracking easier and more enjoyable for people from all walks of life. I will aim to assist students, graduates, young professionals and anyone else interested, to get a grip on their personal finances early-on in life, allowing them to build their wealth plan to retirement, and also giving them an easy way to track their financial performance. I want to develop an intuative app that will make capturing daily transaction details a seamless and easy process.

Target Market(s)

This app must appeal to anyone in need of an easy and intuative solution to track their daily finances and to understand what their current lifestyle will mean for their wealth building..

Industry/Entity Type

Personal finance

Font styles to use
Sans Serif

Requirements
Must have
• Super easy and intuative interface, easy capturing of actual expenses, easy setup of planned income and expenses, visual representation of wealth building over time.
Nice to have
• Would be nice if there's.some way to present the solution in a gaming interface, so capturing daily expenses feels less like a chore and more like a game.
Should not have
• Should not look like a spreadsheet.

```html
<!DOCTYPE html>
<html lang="en">
<head>
<meta charset="utf-8">
<title>Annul Plan 2024</title>
<link rel="stylesheet" href="https://fonts.googleapis.com/css2?family=Inter:wght@300;400;600;700;800&display=swap">
<style>
  :root {
    --header-blue: #7b9fff;
    --month-bar: #3a4a70;
    --category-bar: #5d6f9d;
    --white: #ffffff;
    --year-grey: #dcdcdc;
    --ink: #000000;
    --navy: #2f3d63;
    --label: #3f4a6b;
    --field-border: #5a5f73;
    --button: #3b5ca6;
  }
  * { margin: 0; padding: 0; box-sizing: border-box; }
  html, body { width: 1200px; height: 2379px; overflow: hidden; background: var(--white); }
  body { font-family: "Inter", sans-serif; position: relative; }

  .header { position: absolute; left: 0; top: 0; width: 1200px; height: 611px; background: var(--header-blue); }
  .greeting { position: absolute; left: 91px; top: 100px; font-size: 68px; font-weight: 700; color: var(--white); }
  .plan-title { position: absolute; left: 0; width: 1200px; top: 195px; text-align: center; font-size: 150px; font-weight: 700; color: var(--white); letter-spacing: -1px; line-height: 1; }
  .plan-year { position: absolute; left: 0; width: 1200px; top: 375px; text-align: center; font-size: 150px; font-weight: 700; color: var(--year-grey); line-height: 1; }

  .tab-bar { position: absolute; left: 0; width: 1200px; overflow: hidden; }
  .month-bar { top: 611px; height: 119px; background: var(--month-bar); }
  .category-bar { top: 730px; height: 118px; background: var(--category-bar); }
  .tab { position: absolute; top: 50%; transform: translate(-50%, -50%); white-space: nowrap; font-size: 36px; font-weight: 300; color: var(--white); }
  .tab.active { font-weight: 700; }

  .amount { position: absolute; left: 0; width: 1200px; top: 910px; text-align: center; font-size: 152px; font-weight: 800; color: var(--ink); line-height: 1; }
  .repeat-label { position: absolute; left: 0; width: 1200px; top: 1075px; text-align: center; font-size: 48px; font-weight: 700; color: var(--navy); }

  .field { position: absolute; height: 63px; border: 3px solid var(--field-border); background: var(--white); }
  .field svg { position: absolute; right: 8px; top: 6px; }
  .form-text { position: absolute; font-size: 36px; font-weight: 400; color: var(--label); white-space: nowrap; }

  .submit-button { position: absolute; left: 318px; top: 1414px; width: 722px; height: 72px; border-radius: 36px; background: var(--button); color: var(--white); font-size: 38px; font-weight: 400; display: flex; align-items: center; justify-content: center; }
</style>
</head>
<body>
  <header class="header">
    <p class="greeting">Hi John Doe</p>
    <h1 class="plan-title">Annul Plan</h1>
    <p class="plan-year">2024</p>
  </header>

  <nav class="tab-bar month-bar">
    <span class="tab" style="left:-30px">January</span>
    <span class="tab" style="left:115px">Feb</span>
    <span class="tab" style="left:256px">March</span>
    <span class="tab" style="left:392px">April</span>
    <span class="tab active" style="left:546px">May</span>
    <span class="tab" style="left:704px">June</span>
    <span class="tab" style="left:847px">July</span>
    <span class="tab" style="left:1029px">August</span>
    <span class="tab" style="left:1220px">September</span>
  </nav>

  <nav class="tab-bar category-bar">
    <span class="tab" style="left:22px">Food</span>
    <span class="tab" style="left:175px">Transport</span>
    <span class="tab" style="left:371px">Education</span>
    <span class="tab active" style="left:600px">Grocery</span>
    <span class="tab" style="left:928px">Savings &amp; investments</span>
  </nav>

  <p class="amount">$ 15</p>
  <p class="repeat-label">Repeat Every</p>

  <div class="field" style="left:70px; top:1200px; width:152px;">
    <svg width="34" height="46" viewBox="0 0 34 46"><path d="M6 18 L17 7 L28 18 M6 28 L17 39 L28 28" fill="none" stroke="#000" stroke-width="5" stroke-linecap="round" stroke-linejoin="round"/></svg>
  </div>
  <span class="form-text" style="left:240px; top:1210px;">Months for next</span>
  <div class="field" style="left:535px; top:1200px; width:152px;">
    <svg width="34" height="46" viewBox="0 0 34 46"><path d="M6 18 L17 7 L28 18 M6 28 L17 39 L28 28" fill="none" stroke="#000" stroke-width="5" stroke-linecap="round" stroke-linejoin="round"/></svg>
  </div>
  <span class="form-text" style="left:721px; top:1210px;">years and escavalate with</span>

  <div class="field" style="left:70px; top:1288px; width:152px;"></div>
  <span class="form-text" style="left:240px; top:1298px;">per year</span>

  <div class="submit-button">Submit Now</div>
</body>
</html>
```